Website design for labour force (commercial truck driver) company

Looking for a Wordpress template (or design files in conjunction with a free Wordpress template).
Company tag line:
Tenvora – On Demand, Professional Drivers
Real Drivers | Real Standards | Real Results
Logo design has already been completed and is attached

Company provides contract drivers to trucking companies. Target market is both the trucking companies looking for drivers and drivers looking for work.
Design to encompass header / footer and basic page design, navigation menu, home page, contact page. Customer will add content and additional pages over time.

```html
<!DOCTYPE html>
<html lang="en">
<head>
<meta charset="UTF-8">
<title>Tenvora – On Demand, Professional Drivers</title>
<link href="https://fonts.googleapis.com/css2?family=Poppins:wght@400;500;600;700&display=swap" rel="stylesheet">
<style>
:root{
  --green:#148763;
  --ink:#231f20;
  --black:#0b0b0b;
  --grey-bg:#f4f4f4;
  --text:#333;
  --white:#fff;
  --footer:#0d0d0d;
  --bottom:#161b24;
}
*{box-sizing:border-box;margin:0;padding:0}
html,body{width:1200px;height:3886px;overflow:hidden}
body{font-family:'Poppins',sans-serif;color:var(--text);background:var(--white);position:relative}
.section{position:absolute;left:0;width:1200px}
.btn{position:absolute;display:flex;align-items:center;height:42px;border-radius:21px;background:var(--green);color:var(--white);font-weight:600;font-size:16px;padding-left:14px;width:174px;border:3px solid var(--green)}
.btn .btn-icon{position:absolute;right:0;top:-3px;width:62px;height:42px;border-radius:21px;background:var(--black);border:3px solid var(--green);display:flex;align-items:center;justify-content:center}
.btn.light{background:var(--white);color:var(--green);border-color:var(--white)}
.btn.light .btn-icon{background:var(--white);border-color:var(--green)}
.rule{position:absolute;width:70px;height:6px}
.rule::before{content:"";position:absolute;left:0;top:0;width:56px;height:6px;border-radius:3px;background:var(--green)}
.rule::after{content:"";position:absolute;right:0;top:0;width:6px;height:6px;border-radius:50%;background:var(--green)}
.rule.white::before,.rule.white::after{background:var(--white)}
h2{font-weight:700;color:var(--ink);font-size:38px;line-height:1.1}

.header{top:0;height:89px;border-top:4px solid var(--green);background:var(--white)}
.brand{position:absolute;display:flex;align-items:center;gap:8px;font-weight:700;font-size:29px;color:var(--ink)}
.brand .dot{width:26px;height:26px;border-radius:50%;background:var(--green)}
.header .brand{left:121px;top:20px}
.nav{position:absolute;left:398px;top:34px;display:flex;gap:44px;font-weight:600;font-size:16px;color:var(--ink)}
.header .btn{left:907px;top:23px;width:173px}

.hero{top:89px;height:532px;background:linear-gradient(90deg,#050505 0%,#1a1d22 45%,#3b4a4c 70%,#22503f 100%)}
.hero h1{position:absolute;left:127px;top:175px;color:var(--white);font-size:35px;font-weight:700;line-height:1.12}
.hero .tag{position:absolute;left:127px;top:268px;color:var(--white);font-weight:600;font-size:18px}
.hero .btn{left:127px;top:317px}

.welcome{top:621px;height:504px}
.welcome-photo{position:absolute;left:128px;top:130px;width:450px;height:278px;border-radius:12px;background:linear-gradient(120deg,#7a8690,#a9b2b6 45%,#4f7a6a 70%,#3a3a3a)}
.welcome h2{position:absolute;left:622px;top:85px}
.welcome .rule{left:622px;top:147px}
.welcome p{position:absolute;left:622px;top:170px;width:455px;font-size:15px;line-height:24px}
.welcome .btn{left:622px;top:360px}

.audience{top:1125px;height:215px}
.aud-card{position:absolute;top:0;height:215px;width:462px;color:var(--white)}
.aud-card.companies{left:128px;background:var(--ink);border-radius:0 108px 108px 0}
.aud-card.drivers{left:608px;background:var(--green);border-radius:108px 0 0 108px}
.aud-card h3{position:absolute;font-size:23px;font-weight:500;line-height:27px}
.aud-card p{position:absolute;font-size:14px;line-height:19px;opacity:.9}
.aud-icon{position:absolute;top:38px;width:140px;height:140px;border-radius:50%;display:flex;align-items:center;justify-content:center}

.why{top:1435px;height:560px;background:var(--grey-bg)}
.why h2{position:absolute;left:128px;top:95px}
.why .rule{left:128px;top:158px}
.why p{position:absolute;left:128px;top:182px;width:430px;font-size:15px;line-height:24px}
.why .btn{left:128px;top:380px}
.why-ring{position:absolute;left:578px;top:82px;width:572px;height:572px;border-radius:50%;border:3px solid var(--green);background:var(--grey-bg);z-index:2}
.why-photo{position:absolute;left:18px;top:18px;width:530px;height:530px;border-radius:50%;background:linear-gradient(135deg,#d8e2ea,#b7c4cc 40%,#8a6f5f 60%,#e7ecef)}

.openings{top:1995px;height:545px;background:linear-gradient(180deg,#2a7d5d,#1f8a65 50%,#168a64)}
.openings h2{position:absolute;left:130px;top:110px;color:var(--white)}
.openings .rule{left:130px;top:175px}
.job{position:absolute;top:235px;width:298px;height:176px;border:2px solid rgba(255,255,255,.55);border-radius:8px;padding:30px 28px;color:var(--white)}
.job .co{font-size:12px;font-weight:600}
.job h4{margin-top:12px;font-size:17px;font-weight:600;line-height:22px}
.job .meta{margin-top:18px;font-size:14px;font-weight:500}
.dots{position:absolute;left:553px;top:2463px;display:flex;gap:10px}
.dots span{width:10px;height:10px;border-radius:50%;background:rgba(255,255,255,.45)}
.dots span:first-child{background:var(--white)}

.news{top:2540px;height:670px}
.news h2{position:absolute;left:0;width:1200px;text-align:center;top:105px}
.news .rule{left:565px;top:172px}
.post{position:absolute;top:195px;width:296px;height:365px;background:var(--white);box-shadow:0 4px 18px rgba(0,0,0,.07)}
.post .thumb{height:185px}
.post .date{position:absolute;left:0;top:170px;background:var(--green);color:var(--white);font-size:12px;font-weight:700;padding:10px 12px;border-radius:0 20px 0 0}
.post h4{position:absolute;left:28px;top:222px;width:240px;font-size:19px;font-weight:600;line-height:22px;color:var(--ink)}
.post p{position:absolute;left:28px;top:283px;width:245px;font-size:13px;line-height:19px;color:#555}

.cta{top:3210px;height:262px;background:var(--black)}
.cta-top{position:absolute;left:0;top:0;width:1200px;height:115px;background:var(--white)}
.cta-band{position:absolute;left:0;top:0;width:1072px;height:262px;background:var(--green);border-radius:0 131px 131px 0}
.cta h3{position:absolute;left:128px;top:86px;width:520px;color:var(--white);font-size:25px;font-weight:600;line-height:31px}
.cta p{position:absolute;left:126px;top:163px;width:470px;color:var(--white);font-size:14px;line-height:20px;opacity:.9}
.cta .btn{left:785px;top:107px;width:175px}

.footer{top:3472px;height:354px;background:var(--footer);color:var(--white)}
.footer .brand{left:128px;top:90px;color:var(--white);font-size:34px}
.footer .about{position:absolute;left:127px;top:170px;width:320px;font-size:14px;line-height:24px}
.vline{position:absolute;top:112px;width:1px;height:140px;background:#444}
.footer h5{position:absolute;font-size:20px;font-weight:600}
.links{position:absolute;left:606px;top:150px;font-size:14px;line-height:22px;list-style:none}
.contact-item{position:absolute;left:840px;display:flex;gap:12px;align-items:center;font-size:14px;line-height:19px}
.contact-item .ci{width:36px;height:36px;border-radius:50%;background:var(--green);display:flex;align-items:center;justify-content:center}
.bottom{top:3826px;height:60px;background:var(--bottom);color:#ddd;font-size:14px}
.bottom .legal{position:absolute;left:127px;top:20px;display:flex;gap:46px}
.bottom .social{position:absolute;left:590px;top:24px;display:flex;gap:14px}
.bottom .social span{width:12px;height:12px;border-radius:50%;background:#ddd}
.bottom .copy{position:absolute;right:128px;top:20px}
</style>
</head>
<body>

<header class="section header">
  <div class="brand"><span class="dot"></span>Tenvora</div>
  <nav class="nav"><span>Home</span><span>About</span><span>Services</span><span>Drivers</span><span>Contact</span></nav>
  <div class="btn">Apply Now<span class="btn-icon"><svg width="22" height="14" viewBox="0 0 22 14"><path d="M2 7h17M13 2l6 5-6 5" fill="none" stroke="#148763" stroke-width="2.5" stroke-linecap="round" stroke-linejoin="round"/></svg></span></div>
</header>

<section class="section hero" role="img" aria-label="Smiling truck driver in a green uniform at the wheel of a cab">
  <h1>Tenvora – On Demand,<br>Professional Drivers</h1>
  <div class="tag">Real Drivers &nbsp;| Real Standards | Real Results</div>
  <div class="btn">Contact Us<span class="btn-icon"><svg width="22" height="14" viewBox="0 0 22 14"><path d="M2 7h17M13 2l6 5-6 5" fill="none" stroke="#148763" stroke-width="2.5" stroke-linecap="round" stroke-linejoin="round"/></svg></span></div>
</section>

<section class="section welcome">
  <div class="welcome-photo" role="img" aria-label="Truck driver holding a tablet beside a trailer"></div>
  <h2>Welcome to Tenvora</h2>
  <div class="rule"></div>
  <p>Lorem ipsum dolor sit amet, consectetur adipiscing elit, sed do eiusmod tempor incididunt ut labore et dolore magna aliqua. Quis ipsum suspendisse ultrices gravida. Risus com modo viverra maecenas ausmod tempor incididunt loreut labo re et dolore magna aliqua. Quis ipsum suspendisse ultri ces gravida. Risus com modo viverra maecenas accu msan lacus vel faccumsan lacus vel facilisis.</p>
  <div class="btn">Contact Us<span class="btn-icon"><svg width="22" height="14" viewBox="0 0 22 14"><path d="M2 7h17M13 2l6 5-6 5" fill="none" stroke="#148763" stroke-width="2.5" stroke-linecap="round" stroke-linejoin="round"/></svg></span></div>
</section>

<section class="section audience">
  <div class="aud-card companies">
    <h3 style="left:37px;top:48px">Companies<br>Looking for Drivers</h3>
    <p style="left:37px;top:118px;width:250px">Lorem ipsum dolor sit amcons ectetur adipiscing elit.</p>
    <div class="aud-icon" style="left:299px;background:var(--green)">
      <svg width="70" height="82" viewBox="0 0 70 82" fill="none" stroke="#fff" stroke-width="2.5"><circle cx="35" cy="22" r="14"/><path d="M21 18h28"/><path d="M8 78c0-18 12-30 27-30s27 12 27 30"/><circle cx="35" cy="66" r="13"/><path d="M22 66h26M35 53v26"/></svg>
    </div>
  </div>
  <div class="aud-card drivers">
    <div class="aud-icon" style="left:30px;background:var(--ink)">
      <svg width="82" height="60" viewBox="0 0 82 60" fill="none" stroke="#fff" stroke-width="2.5"><rect x="4" y="6" width="48" height="36" rx="2"/><path d="M52 18h14l10 12v12H52z"/><circle cx="18" cy="48" r="6"/><circle cx="64" cy="48" r="6"/><path d="M12 16h22M12 24h16"/></svg>
    </div>
    <h3 style="left:188px;top:48px">Drivers looking<br>for work</h3>
    <p style="left:188px;top:118px;width:250px">Lorem ipsum dolor sit amcons ectetur adipiscing elit.</p>
  </div>
</section>

<section class="section why">
  <h2>Why Choose Us?</h2>
  <div class="rule"></div>
  <p>Lorem ipsum dolor sit amet, consectetur adipiscing elit, sed do eiusmod tempor incididunt ut labore et dolore magna aliqua. Quis ipsum suspendisse ultrices gravida. Risus com modo viverra maecenas ausmod tempor incididunt loreut labo re et dolore magna aliqua. Quis ipsum suspendisse ultri ces gravida. Risus com modo viverra maecenas accu msan lel facilisis.</p>
  <div class="btn">Contact Us<span class="btn-icon"><svg width="22" height="14" viewBox="0 0 22 14"><path d="M2 7h17M13 2l6 5-6 5" fill="none" stroke="#148763" stroke-width="2.5" stroke-linecap="round" stroke-linejoin="round"/></svg></span></div>
  <div class="why-ring"><div class="why-photo" role="img" aria-label="Driver leaning out of a white truck cab giving a thumbs up"></div></div>
</section>

<section class="section openings" role="img" aria-label="Green-tinted countryside highway with a truck">
  <h2>Latest Openings</h2>
  <div class="rule white"></div>
  <div class="job" style="left:126px"><div class="co">COMPANY NAME</div><h4>Lorem ipsum dolor sit ae consectetur adipisc.</h4><div class="meta">Full Time: Los Angels</div></div>
  <div class="job" style="left:451px"><div class="co">COMPANY NAME</div><h4>Lorem ipsum dolor sit ae consectetur adipisc.</h4><div class="meta">Full Time: Los Angels</div></div>
  <div class="job" style="left:774px"><div class="co">COMPANY NAME</div><h4>Lorem ipsum dolor sit ae consectetur adipisc.</h4><div class="meta">Full Time: Los Angels</div></div>
</section>
<div class="dots"><span></span><span></span><span></span><span></span><span></span></div>

<section class="section news">
  <h2>Latest News</h2>
  <div class="rule"></div>
  <article class="post" style="left:127px">
    <div class="thumb" role="img" aria-label="Woman driver smiling in a truck cab" style="background:linear-gradient(135deg,#6b4a3a,#a88d72 50%,#d9dfe2)"></div>
    <span class="date">JULY 15</span>
    <h4>Lorem ipsum dolor sit ametcon sectetur</h4>
    <p>Lorem ipsum dolor sit ametconse ctetur adipiscing elit, sed do eius mod tempor incididunt.</p>
  </article>
  <article class="post" style="left:452px">
    <div class="thumb" role="img" aria-label="Truck driving along a country road at sunset" style="background:linear-gradient(180deg,#8aa4b8,#d9c08a 45%,#5b7a3d 75%,#3d4d2c)"></div>
    <span class="date">JULY 15</span>
    <h4>Lorem ipsum dolor sit ametcon sectetur</h4>
    <p>Lorem ipsum dolor sit ametconse ctetur adipiscing elit, sed do eius mod tempor incididunt.</p>
  </article>
  <article class="post" style="left:775px">
    <div class="thumb" role="img" aria-label="Driver standing in front of a white truck" style="background:linear-gradient(135deg,#cfe0ee,#7d98b8 50%,#e9edf1)"></div>
    <span class="date">JULY 15</span>
    <h4>Lorem ipsum dolor sit ametcon sectetur</h4>
    <p>Lorem ipsum dolor sit ametconse ctetur adipiscing elit, sed do eius mod tempor incididunt.</p>
  </article>
</section>

<section class="section cta">
  <div class="cta-top"></div>
  <div class="cta-band"></div>
  <h3>Lorem ipsum dolor sit amet, cteturad scing elit sed do eiusmod.</h3>
  <p>Lorem ipsum dolor sit amet, consectetur adipiscing elit, sed do eiusmod tempor incididunt ut labsore et dolore.</p>
  <div class="btn light">Apply Now<span class="btn-icon"><svg width="22" height="14" viewBox="0 0 22 14"><path d="M2 7h17M13 2l6 5-6 5" fill="none" stroke="#148763" stroke-width="2.5" stroke-linecap="round" stroke-linejoin="round"/></svg></span></div>
</section>

<footer class="section footer">
  <div class="brand"><span class="dot"></span>Tenvora</div>
  <p class="about">Lorem ipsum dolor sit amet, consectetur adipiscing elit, sed do eiusmod tempor incididunt ut labore et dolore magna aliquais ipsum suspe.</p>
  <div class="vline" style="left:526px"></div>
  <h5 style="left:606px;top:110px">Links</h5>
  <ul class="links"><li>Home</li><li>About</li><li>Services</li><li>Drivers</li><li>Contact</li></ul>
  <div class="vline" style="left:758px"></div>
  <h5 style="left:840px;top:110px">Contact</h5>
  <div class="contact-item" style="top:160px"><span class="ci"><svg width="18" height="14" viewBox="0 0 18 14" fill="none" stroke="#fff" stroke-width="1.6"><rect x="1" y="1" width="16" height="12" rx="1"/><path d="M1 2l8 6 8-6"/></svg></span><span>Email:<br>hello@tenvora-mail.com</span></div>
  <div class="contact-item" style="top:218px"><span class="ci"><svg width="16" height="16" viewBox="0 0 16 16" fill="none" stroke="#fff" stroke-width="1.6"><path d="M4 1l3 4-2 2a9 9 0 0 0 4 4l2-2 4 3-2 3C6 15 1 10 1 3z"/></svg></span><span>Phone:<br>555 014 2287</span></div>
</footer>

<div class="section bottom">
  <div class="legal"><span>Terms of Use</span><span>Privacy Policy</span><span>Sitemap</span></div>
  <div class="social"><span></span><span></span><span></span><span></span><span></span></div>
  <div class="copy">2025 © All Rights are Reserved.</div>
</div>

</body>
</html>
```